Chiropractic Business Card

I need a business card designed to help me stand apart from my competition. I really like simple, clean designs that appear open and inviting. I would like the designs to incorporate the color blue, green, or both. I really like the attached picture because it highlights that I just don't treat "back pain" and it being a nice computer graphic helps show that I have a modern practice. "Modern practice" meaning merging technology and most current research in my patient care.

My information is:

Wesley Harmon, DC
Phone- (707) 555-0182
Email- drwesleyharmon@mailbox-example.com
Website- www.fernleachiropractic-example.com
Address- 248 Pellham Street, Sonoma, CA 95400

Jpeg and pdf attached of Fernlea Chiropractic logo.
Updates

Atmosphere to be clean lines and solid colors to be have gradient fading, but don't want too much going on with the fading. Simple.

Target Market(s)

Active adults who are health conscious between the ages of 20-70

Industry/Entity Type

Computer

Colors
0455a3
85cae6

Requirements
Must have
• Change color of Fernlea chiropractic logo (maroon) to fit the rest of the design.
Nice to have
• Can separate the running image from the black background to have it work with the design.

```html
<!DOCTYPE html>
<html lang="en">
<head>
<meta charset="utf-8">
<title>Fernlea Chiropractic – Business Card</title>
<link rel="stylesheet" href="https://fonts.googleapis.com/css2?family=Open+Sans:wght@400;600;700&display=swap">
<style>
  :root {
    --page-bg: #e8ecf0;
    --brand-deep: #0455a3;
    --brand-light: #85cae6;
    --card-dark: #1d5c9c;
    --card-mid: #3f86c4;
    --card-pale: #8fbde4;
    --ink-navy: #0b2244;
    --ink-white: #ffffff;
    --accent-pain: #e8454a;
  }
  * { box-sizing: border-box; margin: 0; padding: 0; }
  html, body {
    width: 1200px; height: 900px; overflow: hidden;
    background: var(--page-bg);
    font-family: "Open Sans", Arial, sans-serif;
  }
  .canvas {
    position: relative; width: 1200px; height: 900px;
  }
  .card {
    position: absolute;
    width: 595px; height: 340px;
    border-radius: 4px;
    overflow: hidden;
    box-shadow: 0 10px 28px rgba(10, 40, 80, 0.22);
  }
  .card-front {
    left: 90px; top: 90px;
    background: linear-gradient(200deg, var(--card-pale) 0%, var(--card-mid) 48%, var(--card-dark) 100%);
  }
  .card-back {
    left: 515px; top: 470px;
    background: linear-gradient(200deg, var(--card-pale) 0%, var(--card-mid) 45%, var(--card-dark) 100%);
  }
  .card-sweep {
    position: absolute; inset: 0; width: 100%; height: 100%;
  }
  .front-wordmark {
    position: absolute; left: 0; right: 0; top: 0; bottom: 0;
    display: flex; align-items: center; justify-content: center;
    font-weight: 700; font-size: 46px; letter-spacing: 1px;
    color: var(--brand-deep);
    text-transform: uppercase;
    opacity: 0.75;
  }
  .back-wordmark {
    position: absolute; left: 34px; top: 92px;
    display: flex; align-items: center; gap: 8px;
    font-weight: 700; font-size: 17px; letter-spacing: 0.5px;
    color: var(--ink-white); text-transform: uppercase;
  }
  .back-wordmark .mark-square {
    width: 10px; height: 10px; background: var(--ink-white);
  }
  .figure-area {
    position: absolute; right: 0; top: 0;
    width: 330px; height: 250px;
    background: radial-gradient(ellipse at 55% 50%, rgba(225, 238, 248, 0.75) 0%, rgba(170, 205, 232, 0.45) 45%, rgba(143, 189, 228, 0) 75%);
  }
  .contact-block {
    position: absolute; left: 34px; bottom: 32px;
  }
  .practitioner-name {
    font-weight: 700; font-size: 21px;
    color: var(--ink-navy); text-transform: uppercase;
    margin-bottom: 10px; letter-spacing: 0.3px;
  }
  .contact-list { list-style: none; }
  .contact-list li {
    display: flex; align-items: center; gap: 10px;
    font-size: 12.5px; color: var(--ink-white);
    line-height: 21px;
  }
  .contact-list svg { width: 13px; height: 13px; flex: none; }
</style>
</head>
<body>
<main class="canvas">

  <section class="card card-front" aria-label="Business card front">
    <svg class="card-sweep" viewBox="0 0 595 340" aria-hidden="true">
      <path d="M -20 340 Q 180 150 620 120" fill="none" stroke="rgba(255,255,255,0.18)" stroke-width="1.5"/>
      <path d="M 60 360 Q 280 190 620 180" fill="none" stroke="rgba(255,255,255,0.10)" stroke-width="1.5"/>
    </svg>
    <div class="front-wordmark">Fernlea Chiropractic</div>
  </section>

  <section class="card card-back" aria-label="Business card back">
    <svg class="card-sweep" viewBox="0 0 595 340" aria-hidden="true">
      <path d="M -20 340 Q 200 170 620 150" fill="none" stroke="rgba(255,255,255,0.16)" stroke-width="1.5"/>
    </svg>
    <div class="figure-area" role="img" aria-label="Translucent 3D runner in a sprint start with skeleton visible and red glowing pain points at shoulder, elbow, wrist, hip and knee"></div>

    <div class="back-wordmark"><span class="mark-square"></span>Fernlea Chiropractic</div>

    <div class="contact-block">
      <h1 class="practitioner-name">Wesley Harmon, DC</h1>
      <ul class="contact-list">
        <li>
          <svg viewBox="0 0 24 24" aria-hidden="true"><path fill="#fff" d="M6.6 10.8a15.1 15.1 0 0 0 6.6 6.6l2.2-2.2a1 1 0 0 1 1-.25 11.4 11.4 0 0 0 3.6.57 1 1 0 0 1 1 1V20a1 1 0 0 1-1 1A17 17 0 0 1 3 4a1 1 0 0 1 1-1h3.5a1 1 0 0 1 1 1c0 1.25.2 2.45.57 3.6a1 1 0 0 1-.25 1z"/></svg>
          (707) 555-0182
        </li>
        <li>
          <svg viewBox="0 0 24 24" aria-hidden="true"><path fill="#fff" d="M3 5h18v14H3z"/><path fill="none" stroke="#1d5c9c" stroke-width="2" d="M3 6l9 7 9-7"/></svg>
          drwesleyharmon@mailbox-example.com
        </li>
        <li>
          <svg viewBox="0 0 24 24" aria-hidden="true"><circle cx="10" cy="10" r="6" fill="none" stroke="#fff" stroke-width="2.5"/><path d="M14.5 14.5L21 21" stroke="#fff" stroke-width="3"/></svg>
          www.fernleachiropractic-example.com
        </li>
        <li>
          <svg viewBox="0 0 24 24" aria-hidden="true"><path fill="#fff" d="M12 3l10 9h-3v9h-5v-6h-4v6H5v-9H2z"/></svg>
          248 Pellham Street, Sonoma, CA 95400
        </li>
      </ul>
    </div>
  </section>

</main>
</body>
</html>
```